Velmora Water Purification

We need a website set up on a "Free account" WordPress platform. (This is the type of Wordpress site that you can sign up for and create online for free (not a server-hosted type.)
The website will be for a water purification company. They install devices in homes to purify the water for safer drinking, bathing, and cleaning.
Our logo is attached. Please keep color scheme of the website consistent with the logo.
Water Purification

```html
<!DOCTYPE html>
<html lang="en">
<head>
<meta charset="utf-8">
<title>Velmora Water Purification</title>
<link href="https://fonts.googleapis.com/css2?family=Lato:wght@400;700;900&family=Montserrat:wght@400;600&family=Raleway:wght@300;400;500&display=swap" rel="stylesheet">
<style>
:root{
  --blue:#5ea6d6;
  --blue-soft:#78b6e0;
  --blue-pale:#e6f2fa;
  --navy:#1b2a5c;
  --footer:#6aaedb;
  --footer-base:#8ccbf0;
  --grey-bg:#f1f2f4;
  --text:#3b3f48;
  --muted:#8a8f99;
  --white:#ffffff;
}
*{margin:0;padding:0;box-sizing:border-box}
html,body{width:1200px;height:3689px;overflow:hidden;background:var(--white)}
body{position:relative;font-family:'Lato',sans-serif;color:var(--text)}
.abs{position:absolute}

/* hero */
.hero{left:0;top:0;width:1200px;height:627px;background:linear-gradient(115deg,#1f3a3a 0%,#27503f 40%,#1d3c47 70%,#142b3a 100%)}
.topbar{left:0;top:0;width:1200px;height:44px;display:flex;justify-content:flex-end;align-items:center;gap:40px;padding-right:140px;color:#dfe8ee;font-size:11px;font-family:'Lato',sans-serif}
.topbar span{display:flex;align-items:center;gap:8px}
.nav{left:0;top:44px;width:1200px;height:69px;background:var(--white);display:flex;align-items:center}
.brand{position:absolute;left:98px;top:16px;display:flex;align-items:center;gap:10px;font-family:'Raleway',sans-serif;font-weight:500;font-size:17px;color:var(--navy)}
.brand i{width:34px;height:34px;border-radius:50%;background:var(--blue);display:block}
.menu{position:absolute;left:278px;top:0;display:flex;height:69px}
.menu a{display:block;padding:24px 18px 0;font-size:14px;color:#777;text-decoration:none;font-family:'Lato',sans-serif}
.menu a.on{color:var(--blue);border-top:3px solid var(--blue);padding-top:21px}
.search{position:absolute;left:830px;top:24px;width:135px;height:22px;border:1px solid #ddd;font-size:9px;color:#aaa;padding:5px 8px}
.social{position:absolute;left:984px;top:24px;display:flex;gap:6px}
.social i{width:20px;height:20px;border-radius:50%;background:#999;display:block}
.hero-title{left:98px;top:195px;font-family:'Montserrat',sans-serif;font-weight:600;font-size:40px;letter-spacing:7px;line-height:50px;color:var(--white)}
.hero-title em{font-style:normal;color:#7fc3ee}
.hero-copy{left:98px;top:408px;width:330px;font-size:16px;line-height:20px;color:#e8eef2}
.btn-outline{left:98px;top:514px;width:150px;height:32px;border:2px solid #7fc3ee;color:#fff;font-size:11px;letter-spacing:2px;display:flex;align-items:center;justify-content:center}
.quote{left:811px;top:167px;width:288px;height:403px;background:var(--white);box-shadow:0 4px 14px rgba(0,0,0,.3)}
.quote h3{height:40px;background:var(--blue-soft);color:#fff;font-family:'Montserrat',sans-serif;font-weight:400;font-size:11px;letter-spacing:2px;text-align:center;line-height:40px}
.field{position:absolute;font-size:9px;color:#777}
.field b{display:block;font-weight:400;margin-bottom:5px}
.field i{display:block;height:26px;background:#ececec;font-style:normal;font-size:8px;color:#888;padding:8px 6px}
.send{left:75px;top:349px;width:138px;height:28px;background:var(--navy);color:#fff;font-size:10px;letter-spacing:2px;text-align:center;line-height:28px}

/* award */
.badge{left:155px;top:710px;width:175px;height:175px;border-radius:50%;background:#3f74b8}
.award-head{left:590px;top:720px;font-family:'Raleway',sans-serif;font-size:21px;letter-spacing:1px;color:var(--blue)}
.award-copy{left:590px;top:775px;width:560px;font-family:'Raleway',sans-serif;font-weight:300;font-size:19px;line-height:36px;color:#6da9d2}

/* features */
.feature{top:1082px;width:240px;text-align:center}
.feature svg{display:block;margin:0 auto}
.feature h4{margin-top:14px;font-family:'Montserrat',sans-serif;font-weight:400;font-size:14px;letter-spacing:3px;color:var(--blue)}
.feature p{margin-top:6px;font-size:10px;line-height:13px;color:#999}
.feature span{display:inline-block;margin-top:16px;border:1px solid var(--blue);color:var(--blue);font-size:7px;letter-spacing:1px;padding:4px 12px}

/* testimonials */
.testi-band{left:0;top:1438px;width:1200px;height:475px;background:var(--grey-bg)}
.video{left:15px;top:1466px;width:600px;height:364px;background:linear-gradient(120deg,#c9dfee 0%,#e6d3c6 35%,#a9cde6 70%,#5e93bd 100%)}
.video-caption{left:15px;top:1744px;width:600px;height:86px;background:rgba(20,30,50,.75);padding:24px 22px;color:#fff}
.video-caption h5{font-family:'Lato',sans-serif;font-weight:900;font-size:16px;letter-spacing:1px}
.video-caption p{font-size:15px;font-weight:700;margin-top:4px}
.play{left:273px;top:1607px;width:84px;height:70px;background:rgba(120,170,210,.8)}
.card{left:642px;width:497px;height:104px;background:var(--white);padding:18px 20px 0 66px}
.card .q{position:absolute;left:18px;top:14px;font-family:Georgia,serif;font-size:50px;line-height:50px;color:#dcdcdc}
.card p{font-size:11px;line-height:15px;color:#333}
.card small{display:block;margin-top:10px;font-size:11px;color:var(--blue);letter-spacing:1px}
.dots{left:1048px;top:1851px;display:flex;gap:6px}
.dots i{width:12px;height:12px;border-radius:50%;background:#d4d8de;display:block}
.dots i.on{background:var(--blue)}

/* why bar */
.why{left:0;top:1923px;width:1200px;height:64px;background:#f7f7f7}
.why p{position:absolute;left:295px;top:22px;font-size:17px;letter-spacing:1px;color:#9aa0a8}
.why span{position:absolute;left:818px;top:17px;width:142px;height:36px;background:var(--blue-soft);color:#fff;font-size:9px;letter-spacing:1px;line-height:36px;padding-left:14px}
.why span b{position:absolute;right:0;top:0;width:34px;height:36px;background:#8ec4e8;text-align:center;font-size:14px}

/* split */
.split-left{left:0;top:1987px;width:600px;height:391px;background:linear-gradient(120deg,#b6d4ea 0%,#9cc4e2 50%,#7eb0d8 100%)}
.split-right{left:600px;top:1987px;width:600px;height:391px;background:linear-gradient(120deg,#7ab0da 0%,#5d9ed0 50%,#6ea9d6 100%)}
.split-text{top:2087px;width:600px;text-align:center;color:var(--navy)}
.split-text h2{font-family:'Lato',sans-serif;font-weight:900;font-size:50px;line-height:56px}
.split-text h6{font-size:18px;font-weight:700;margin-top:8px}
.split-text p{font-size:17px;font-weight:700;margin-top:18px;line-height:22px}

/* blog */
.blog-photo{left:504px;top:2378px;width:696px;height:691px;background:linear-gradient(135deg,#f4f4f4 0%,#e9ecef 40%,#dde8f0 70%,#cfdbe6 100%)}
.blog-fade{left:0;top:2378px;width:560px;height:691px;background:var(--white)}
.blog-head{left:40px;top:2448px;font-family:'Lato',sans-serif;font-weight:700;font-size:23px;line-height:28px;color:var(--navy)}
.blog-copy{left:40px;top:2530px;width:440px;font-size:12.5px;font-weight:700;line-height:17px;color:#333}
.post{left:8px;width:528px;height:106px;background:var(--white);box-shadow:0 1px 4px rgba(0,0,0,.12);padding:26px 0 0 15px}
.post p{font-size:10px;line-height:14px;width:420px;color:#333}
.post small{display:flex;align-items:center;gap:6px;margin-top:16px;font-size:9px;color:#333}
.date{position:absolute;left:459px;top:22px;width:69px;text-align:center;color:#fff}
.date b{display:block;height:36px;background:var(--blue);font-size:22px;line-height:36px}
.date i{display:block;height:20px;background:#a8d2ee;font-style:normal;font-size:10px;line-height:20px}

/* footer */
.footer{left:0;top:3069px;width:1200px;height:497px;background:var(--footer);color:#fff}
.footer .rule{position:absolute;top:0;width:1px;height:497px;background:rgba(255,255,255,.3)}
.footer h4{position:absolute;top:62px;font-family:'Lato',sans-serif;font-weight:700;font-size:17px;letter-spacing:1px;display:flex;align-items:center;gap:10px}
.f-text{position:absolute;font-size:12px;line-height:18px}
.links{position:absolute;left:417px;top:212px;font-size:12px;letter-spacing:1px;line-height:27px}
.links a{display:block;color:#fff;text-decoration:underline}
.fsocial{position:absolute;left:98px;top:398px;display:flex;gap:26px}
.fsocial i{width:11px;height:11px;border-radius:50%;background:#fff;display:block}
.input{position:absolute;left:843px;background:#8cc4ea;font-size:12px;padding:12px 14px}
.fbtn{position:absolute;left:843px;top:382px;width:148px;height:36px;background:#a7d4f1;font-size:10px;letter-spacing:1px;text-align:center;line-height:36px}
.base{left:0;top:3566px;width:1200px;height:123px;background:var(--footer-base)}
.base p{position:absolute;right:40px;top:58px;font-size:8px;color:#fff;letter-spacing:.5px}
</style>
</head>
<body>

<section class="abs hero" role="img" aria-label="Photograph of a hand pouring water onto a young green plant"></section>
<div class="abs topbar">
  <span><svg width="9" height="12" viewBox="0 0 9 12"><path d="M4.5 0C2 0 0 2 0 4.5 0 8 4.5 12 4.5 12S9 8 9 4.5C9 2 7 0 4.5 0zm0 6.3a1.8 1.8 0 110-3.6 1.8 1.8 0 010 3.6z" fill="#dfe8ee"/></svg>418 Alder Lane Brookfield, WI 54020</span>
  <span><svg width="8" height="12" viewBox="0 0 8 12"><rect x="0.5" y="0.5" width="7" height="11" rx="1.2" fill="none" stroke="#dfe8ee"/><circle cx="4" cy="9.5" r=".8" fill="#dfe8ee"/></svg>(014) 782 - 3316 or 555 - 019 4471</span>
  <span><svg width="12" height="9" viewBox="0 0 12 9"><rect x=".5" y=".5" width="11" height="8" fill="none" stroke="#dfe8ee"/><path d="M.5.5L6 5 11.5.5" fill="none" stroke="#dfe8ee"/></svg>contact@velmorawater.com</span>
</div>
<header class="abs nav">
  <div class="brand"><i></i>Velmora</div>
  <nav class="menu"><a class="on">Home</a><a>About</a><a>Services</a><a>Faq</a><a>Blog</a><a>Contact</a></nav>
  <div class="search">Search</div>
  <div class="social"><i></i><i></i><i></i><i></i></div>
</header>
<h1 class="abs hero-title">CRYSTAL<br>CLEAR<br>PURITY IN<br><em>EVERY DROP</em></h1>
<p class="abs hero-copy">Lorem ipsum dolor set duroorem ipsum dolor set duro o set duroorem ipsset duro set duroorem ipsum ...</p>
<div class="abs btn-outline">EXPLORE</div>

<form class="abs quote">
  <h3>GET A QUOTE NOW</h3>
  <div class="field" style="left:18px;top:58px;width:118px"><b>Name</b><i></i></div>
  <div class="field" style="left:152px;top:58px;width:118px"><b>Email</b><i></i></div>
  <div class="field" style="left:18px;top:120px;width:252px"><b>Purpose of Contact</b><i>Estimates</i></div>
  <div class="field" style="left:18px;top:182px;width:118px"><b>Select Service</b><i>Select</i></div>
  <div class="field" style="left:152px;top:182px;width:118px"><b>Phone</b><i></i></div>
  <div class="field" style="left:18px;top:244px;width:252px"><b>Message</b><i style="height:50px"></i></div>
  <div class="abs send">SEND</div>
</form>

<div class="abs badge" role="img" aria-label="Award badge"></div>
<h2 class="abs award-head">A GLOBAL AWARD-WINNING BRAND</h2>
<p class="abs award-copy">We offer upfront pricing and satisfaction guarantee since we're so confident about the quality of our work.We offer upfront pricing and satisfaction guarantee.We are a business to create long term relationships with all customers who use our services. We strive to provide</p>

<svg width="0" height="0" style="position:absolute"><defs><linearGradient id="drop" x1="0" y1="0" x2="0" y2="1"><stop offset="0" stop-color="#e6f2fb"/><stop offset="1" stop-color="#b8d8ef"/></linearGradient></defs></svg>

<div class="abs feature" style="left:182px">
  <svg width="150" height="200" viewBox="0 0 150 200"><path d="M75 0 C60 50 0 95 0 135 A75 65 0 0 0 150 135 C150 95 90 50 75 0Z" fill="url(#drop)"/>
    <g fill="none" stroke="#3f7fb8" stroke-width="3"><circle cx="75" cy="125" r="18"/><path d="M68 143v10h14v-10M70 157h10M75 95v-10M50 105l-7-7M100 105l7-7M45 125H35M105 125h10"/></g></svg>
  <h4>SERVICES</h4><p>Lorem ipsum dolor set duroorem<br>lorem dolor set duro o set</p><span>READ MORE</span>
</div>
<div class="abs feature" style="left:480px">
  <svg width="150" height="200" viewBox="0 0 150 200"><path d="M75 0 C60 50 0 95 0 135 A75 65 0 0 0 150 135 C150 95 90 50 75 0Z" fill="url(#drop)"/>
    <path d="M75 140 L55 120 A11 11 0 0 1 75 104 A11 11 0 0 1 95 120Z" fill="#3f7fb8"/>
    <path d="M40 130 Q50 150 75 152 Q100 150 110 130" fill="none" stroke="#3f7fb8" stroke-width="5"/></svg>
  <h4>CUSTOMERS</h4><p>Lorem ipsum dolor set duroorem<br>lorem dolor set duro o set</p><span>READ MORE</span>
</div>
<div class="abs feature" style="left:792px">
  <svg width="150" height="200" viewBox="0 0 150 200"><path d="M75 0 C60 50 0 95 0 135 A75 65 0 0 0 150 135 C150 95 90 50 75 0Z" fill="url(#drop)"/>
    <g fill="none" stroke="#3f7fb8" stroke-width="7" stroke-dasharray="6 5"><circle cx="68" cy="128" r="16"/><circle cx="94" cy="106" r="10"/></g>
    <circle cx="68" cy="128" r="6" fill="#3f7fb8"/><circle cx="94" cy="106" r="4" fill="#3f7fb8"/></svg>
  <h4>TECHNOLOGY</h4><p>Lorem ipsum dolor set duroorem<br>lorem dolor set duro o set</p><span>READ MORE</span>
</div>

<section class="abs testi-band"></section>
<div class="abs video" role="img" aria-label="Photograph of a woman splashing clean water on her face"></div>
<div class="abs play"><svg width="84" height="70" viewBox="0 0 84 70"><path d="M34 22 L54 35 L34 48Z" fill="#fff"/></svg></div>
<div class="abs video-caption"><h5>THE FUNCTIONING OF THE WATER PURIFICATION</h5><p>Ut enim ad minim veniam, quis nostrud exercitation ullamco la</p></div>

<div class="abs card" style="top:1470px"><span class="q">&ldquo;</span><p>Ut enim ad minim veniam, quis nostrud exercitation ullamco laboris nisi ut aliquip ex ea commodo consequat. Duis aute irure dolor</p><small>MARK ELLISON &nbsp;|&nbsp; ST. TEXAS</small></div>
<div class="abs card" style="top:1598px"><span class="q">&ldquo;</span><p>Ut enim ad minim veniam, quis nostrud exercitation ullamco laboris nisi ut aliquip ex ea commodo consequat. Duis aute irure dolor</p><small>MARK ELLISON &nbsp;|&nbsp; ST. TEXAS</small></div>
<div class="abs card" style="top:1728px"><span class="q">&ldquo;</span><p>Ut enim ad minim veniam, quis nostrud exercitation ullamco laboris nisi ut aliquip ex ea commodo consequat. Duis aute irure dolor</p><small>MARK ELLISON &nbsp;|&nbsp; ST. TEXAS</small></div>
<div class="abs dots"><i></i><i></i><i class="on"></i><i></i><i></i></div>

<section class="abs why"><p>Why Choose Velmora Water Purification?</p><span>CONTACT US NOW<b>&rsaquo;</b></span></section>

<div class="abs split-left" role="img" aria-label="Photograph of a technician installing a water filter cartridge"></div>
<div class="abs split-right" role="img" aria-label="Photograph of a plumber working under a kitchen sink"></div>
<svg class="abs" style="left:578px;top:1987px" width="44" height="22" viewBox="0 0 44 22"><path d="M0 0H44L22 22Z" fill="#f7f7f7"/></svg>
<div class="abs split-text" style="left:0"><h2>24/7</h2><h6>CUSTOMER SUPPORT HELPLINE</h6><p>Our support service is available 24 hours a day,<br>7 days a week to help you buy your tickets.</p></div>
<div class="abs split-text" style="left:600px"><h2>GET ESTIMATE</h2><h6>AVAILABLE 24/7 ALL OVER THE U.S.</h6><p>Our support service is available 24 hours a day,<br>7 days a week to help you buy your tickets.</p></div>

<div class="abs blog-photo" role="img" aria-label="Photograph of a mother pouring filtered water into a glass for her daughter in a bright kitchen"></div>
<div class="abs blog-fade"></div>
<h2 class="abs blog-head">Read our expertly written blog<br>or follow us on social media</h2>
<p class="abs blog-copy">Lorem ipsum dolor sit amet, consectetur adipiscing elit, sed do eius-mod tempor incididunt ut labore et dolore magna aliqua. Ut enim ad minim veniam, quis nostrud exercitation ullamco laboris nisi ut aliquip ex ea commodo consequat. Duis aute irure dolor</p>

<article class="abs post" style="top:2643px"><p>Ut enim ad minim veniam, quis nostrud exercitation ullamco laboris nisi ut aliquip ex ea commodo consequat. Duis aute irure dolor</p><small><svg width="10" height="10" viewBox="0 0 10 10"><circle cx="5" cy="5" r="4.3" fill="none" stroke="#333"/><path d="M5 2.5V5h2" fill="none" stroke="#333"/></svg>In &nbsp;Lorem Ipsum, Training</small><div class="date"><b>20</b><i>Dec</i></div></article>
<article class="abs post" style="top:2766px"><p>Ut enim ad minim veniam, quis nostrud exercitation ullamco laboris nisi ut aliquip ex ea commodo consequat. Duis aute irure dolor</p><small><svg width="10" height="10" viewBox="0 0 10 10"><circle cx="5" cy="5" r="4.3" fill="none" stroke="#333"/><path d="M5 2.5V5h2" fill="none" stroke="#333"/></svg>In &nbsp;Lorem Ipsum, Training</small><div class="date"><b>10</b><i>Dec</i></div></article>
<article class="abs post" style="top:2897px"><p>Ut enim ad minim veniam, quis nostrud exercitation ullamco laboris nisi ut aliquip ex ea commodo consequat. Duis aute irure dolor</p><small><svg width="10" height="10" viewBox="0 0 10 10"><circle cx="5" cy="5" r="4.3" fill="none" stroke="#333"/><path d="M5 2.5V5h2" fill="none" stroke="#333"/></svg>In &nbsp;Lorem Ipsum, Training</small><div class="date"><b>25</b><i>Dec</i></div></article>

<footer class="abs footer">
  <span class="rule" style="left:393px"></span><span class="rule" style="left:787px"></span>
  <h4 style="left:40px">GET IN TOUCH WITH US</h4>
  <p class="f-text" style="left:40px;top:165px;width:320px">5120 Harbor Ridge Road, Suite 210,<br>Lakemont, OR 97301</p>
  <p class="f-text" style="left:40px;top:222px">(014) 782 - 3316</p>
  <p class="f-text" style="left:40px;top:258px">contact@velmorawater.com</p>
  <div class="fsocial"><i></i><i></i><i></i><i></i><i></i></div>

  <h4 style="left:410px"><svg width="18" height="18" viewBox="0 0 18 18"><path d="M11 1l6 6-3 1-3 3 1 4-2 1-4-4-5 5-1-1 5-5-4-4 1-2 4 1 3-3z" fill="#fff"/></svg>ADDITIONAL RESEARCH LINKS</h4>
  <p class="f-text" style="left:417px;top:122px;width:340px">Ut enim ad minim veniam, quis nostrud exercitation ullamco laboris Ut enim ad minim veniam, quis nostrud exercitation ullamco laboris nisi ut alinim</p>
  <div class="links"><a>EMERGENCY SERVICE</a><a>AVAILABLE 24/7</a><a>TRUSTED &amp; RECOMMENDED</a><a>LICENSED &amp; INSURED</a><a>FULL SERVICE PLUMBING</a><a>FREE ESTIMATES</a></div>

  <h4 style="left:878px"><svg width="18" height="18" viewBox="0 0 18 18"><path d="M3 10V8a6 6 0 0112 0v2" fill="none" stroke="#fff" stroke-width="1.6"/><rect x="2" y="9" width="3" height="6" rx="1" fill="#fff"/><rect x="13" y="9" width="3" height="6" rx="1" fill="#fff"/></svg>QUICK CONTACT</h4>
  <div class="input" style="top:147px;width:314px;height:42px">Email Address*</div>
  <div class="input" style="top:200px;width:314px;height:160px">Describe briefly*</div>
  <div class="fbtn">CONTACT US NOW</div>
</footer>
<div class="abs base"><p>&copy; 2017 VELMORA WATER PURIFICATION. All Rights Reserved</p></div>

</body>
</html>
```